LumaPeak business card

We are a performing arts company providing training (to both kids and adults) as well as performers for events. We hope to bring joy and confidence on stage to the people we train, as well as joy to the audience when our artistes perform. Designs should convey the joy, confidence and vibrancy on stage. Design business card using the attached logo. Card to include name, mobile tel, email address, company address, and website. Double sided. To also include the following list of what the company does:
• Training & Enrichment
• Private & Corporate Entertainment
- Music composition & production

Industry/Entity Type

Training

Contact Information for Business Card

Card to include name, mobile tel, email address, company address, and website. Double sided. To also include the following list of what the company does:
• Training & Enrichment

Requirements
Nice to have
• Card need not be the traditional rectangular in shape but not too outrageous.

```html
<!DOCTYPE html>
<html lang="en">
<head>
<meta charset="utf-8">
<title>LumaPeak business card</title>
<link rel="stylesheet" href="https://fonts.googleapis.com/css2?family=Arimo:wght@400;700&display=swap">
<style>
  :root {
    --bg: #3a3d42;
    --card: #f7fbfc;
    --ink: #1d1d1f;
    --accent: #e0246f;
    --brand: #4a2a8c;
    --tag: #3b3fa8;
    --icon-bg: #111214;
  }
  * { margin: 0; padding: 0; box-sizing: border-box; }
  html, body { width: 1200px; height: 960px; overflow: hidden; }
  body {
    background: var(--bg);
    font-family: "Arimo", Arial, sans-serif;
    color: var(--ink);
    display: flex;
    align-items: center;
    justify-content: center;
    gap: 80px;
  }
  .card {
    position: relative;
    width: 400px;
    height: 700px;
    background: var(--card);
    border-radius: 28px;
    box-shadow: 0 14px 30px rgba(0,0,0,.35);
  }
  .brand {
    position: absolute;
    top: 120px;
    left: 0;
    right: 0;
    text-align: center;
  }
  .brand-row {
    display: inline-flex;
    align-items: center;
    gap: 12px;
  }
  .brand-mark {
    width: 22px;
    height: 22px;
    border-radius: 50%;
    background: var(--accent);
  }
  .brand-name {
    font-size: 58px;
    font-weight: 700;
    color: var(--brand);
    letter-spacing: -1px;
  }
  .brand-tagline {
    margin-top: 6px;
    font-size: 19px;
    color: var(--tag);
    font-style: italic;
  }
  .services {
    position: absolute;
    top: 390px;
    left: 48px;
    list-style: none;
    font-size: 21px;
    line-height: 1.35;
  }
  .holder-name {
    position: absolute;
    top: 370px;
    left: 48px;
    font-size: 36px;
    color: var(--accent);
  }
  .contacts {
    position: absolute;
    left: 48px;
    bottom: 80px;
    list-style: none;
    font-size: 21px;
  }
  .contacts li {
    display: flex;
    align-items: center;
    gap: 12px;
    height: 34px;
  }
  .contact-icon {
    width: 24px;
    height: 24px;
    flex: none;
  }
</style>
</head>
<body>

<section class="card card-back">
  <div class="brand">
    <div class="brand-row"><span class="brand-mark"></span><span class="brand-name">LumaPeak</span></div>
    <p class="brand-tagline">delighting in the arts</p>
  </div>
  <ul class="services">
    <li>Training &amp; Enrichment</li>
    <li>Private &amp; Corporate Entertainment</li>
    <li>Music composition &amp; production</li>
  </ul>
</section>

<section class="card card-front">
  <div class="brand">
    <div class="brand-row"><span class="brand-mark"></span><span class="brand-name">LumaPeak</span></div>
    <p class="brand-tagline">delighting in the arts</p>
  </div>
  <p class="holder-name">Your Name</p>
  <ul class="contacts">
    <li>
      <svg class="contact-icon" viewBox="0 0 24 24" aria-hidden="true"><rect width="24" height="24" rx="4" fill="var(--icon-bg)"/><rect x="8" y="4" width="8" height="16" rx="1.5" fill="none" stroke="var(--accent)" stroke-width="2"/></svg>
      055-41260000
    </li>
    <li>
      <svg class="contact-icon" viewBox="0 0 24 24" aria-hidden="true"><rect width="24" height="24" rx="4" fill="var(--icon-bg)"/><path d="M7 5l3 0 1 4-2 1.5a8 8 0 0 0 4.5 4.5L15 13l4 1v3c-6 1-13-6-12-12z" fill="var(--accent)"/></svg>
      776-52318800
    </li>
    <li>
      <svg class="contact-icon" viewBox="0 0 24 24" aria-hidden="true"><rect width="24" height="24" rx="4" fill="var(--icon-bg)"/><rect x="5" y="7" width="14" height="10" fill="none" stroke="var(--accent)" stroke-width="2"/><path d="M5 7l7 6 7-6" fill="none" stroke="var(--accent)" stroke-width="2"/></svg>
      hello@lumapeak.com
    </li>
    <li>
      <svg class="contact-icon" viewBox="0 0 24 24" aria-hidden="true"><rect width="24" height="24" rx="4" fill="var(--icon-bg)"/><circle cx="12" cy="12" r="7" fill="none" stroke="var(--accent)" stroke-width="2"/><path d="M5 12h14M12 5c-3 4-3 10 0 14M12 5c3 4 3 10 0 14" fill="none" stroke="var(--accent)" stroke-width="1.5"/></svg>
      www.lumapeak.com
    </li>
    <li>
      <svg class="contact-icon" viewBox="0 0 24 24" aria-hidden="true"><rect width="24" height="24" rx="4" fill="var(--icon-bg)"/><path d="M12 20s-6-6-6-10a6 6 0 0 1 12 0c0 4-6 10-6 10z" fill="var(--accent)"/><circle cx="12" cy="10" r="2.2" fill="var(--icon-bg)"/></svg>
      4512, elm grove street MI 3300 US
    </li>
  </ul>
</section>

</body>
</html>
```